Harborvale Ventures brochure for Investment partnership, young harold pembly

We need a brochure design to attract new investors for our investing partnership Called Harborvale Ventures. We are based in New Orleans, La. We primarily invest in stocks, bonds, and crypto but venture out into other categories as well. We would like to see designs with the black and gold like our logo. The final design should say new, fresh, sleek, tech, and honorable. BROUCHURE WILL BE 4 pages.or one folded sheet a paparer if that makes sense.
Updates

A chart showing Harborvale Ventures gains since 2019 28.6 percent and the TR 400 gAINS 7.1 PERCENT

Target Market(s)

Probable Investors

Industry/Entity Type

Financial Planning

Colors

Designer to choose only greyscale colors for use in the design.

Requirements
Must have
• Black and Gold accent. Stock market feel. Sleek, High tech, innovative, Intellgent design.
Nice to have
• Page colors possibly black.
Should not have
• Boring, Old school,

```html
<!DOCTYPE html>
<html lang="en">
<head>
<meta charset="utf-8">
<title>Harborvale Ventures – Brochure Spread</title>
<link href="https://fonts.googleapis.com/css2?family=Tinos:wght@400;700&display=swap" rel="stylesheet">
<style>
  :root {
    --backdrop: #5c5c5c;
    --ink: #111111;
    --black: #0b0b0b;
    --paper: #f1f1f3;
    --paper-shade: #dcdce0;
    --gold: #b39a3a;
    --gold-light: #d8c470;
    --gold-deep: #8c7624;
    --white: #ffffff;
    --text-dark: #222222;
    --photo-blue: #3d5570;
  }
  * { margin: 0; padding: 0; box-sizing: border-box; }
  html, body { width: 1200px; height: 789px; overflow: hidden; }
  body {
    background: var(--backdrop);
    font-family: "Tinos", "Times New Roman", serif;
    position: relative;
  }
  .page {
    position: absolute;
    top: 26px;
    width: 520px;
    height: 736px;
    overflow: hidden;
  }
  /* ---------- Back cover ---------- */
  .back-cover {
    left: 80px;
    background: linear-gradient(160deg, var(--paper) 0%, #e9e9ec 55%, var(--paper-shade) 100%);
  }
  .about-label {
    position: absolute; left: 48px; top: 56px;
    color: var(--gold); font-weight: 700; font-size: 24px; letter-spacing: 0.5px;
  }
  .about-heading {
    position: absolute; left: 48px; top: 86px;
    color: var(--ink); font-size: 16px; font-weight: 400; letter-spacing: 0.4px;
  }
  .about-rule {
    position: absolute; left: 48px; top: 110px; width: 400px; height: 2px;
    background: var(--gold);
  }
  .about-copy {
    position: absolute; left: 48px; top: 124px; width: 300px;
    font-size: 12px; line-height: 1.25; color: var(--text-dark); text-align: justify;
  }
  .about-photo {
    position: absolute; left: 80px; top: 250px; width: 310px; height: 300px;
    background: linear-gradient(180deg, #cfcfcf 0%, #8a8a8a 45%, #5a5a5a 75%, #9a9a9a 100%);
    z-index: 2;
  }
  .back-panel {
    position: absolute; right: 0; top: 430px; width: 200px; height: 306px;
    background: var(--black);
    z-index: 1;
  }
  .back-panel .gold-band {
    position: absolute; left: 0; top: 120px; width: 100%; height: 44px;
    background: linear-gradient(90deg, var(--gold-deep), var(--gold-light), var(--gold));
    clip-path: polygon(0 30%, 100% 0, 100% 70%, 0 100%);
  }
  .back-panel .wordmark {
    position: absolute; left: 0; right: 0; top: 196px;
    text-align: center; color: var(--gold); font-size: 17px; letter-spacing: 1.5px;
    text-transform: uppercase; line-height: 1.2;
  }
  .contact-list {
    position: absolute; left: 48px; top: 600px; width: 260px; list-style: none;
    font-size: 12px; color: var(--text-dark);
  }
  .contact-list li { display: flex; align-items: flex-start; gap: 10px; margin-bottom: 12px; }
  .contact-list svg { flex: 0 0 12px; margin-top: 2px; }
  .contact-list .web { letter-spacing: 1px; white-space: nowrap; }

  /* ---------- Front cover ---------- */
  .front-cover { left: 600px; background: var(--black); }
  .front-header {
    position: absolute; left: 0; top: 0; width: 100%; height: 150px;
    background: var(--black);
    display: flex; flex-direction: column; align-items: center; justify-content: center;
  }
  .front-header .wordmark {
    color: var(--gold); font-size: 36px; letter-spacing: 3px; text-transform: uppercase;
    text-align: center; line-height: 1.1;
  }
  .front-header .wordmark-sub {
    display: block; font-size: 18px; letter-spacing: 8px;
  }
  .front-photo {
    position: absolute; left: 0; top: 150px; width: 100%; height: 330px;
    background:
      radial-gradient(circle at 45% 65%, rgba(255,255,255,0.85) 0%, rgba(255,255,255,0) 22%),
      linear-gradient(100deg, #e8e8ea 0%, #b9bcc2 30%, var(--photo-blue) 70%, #1e2c3e 100%);
  }
  .tagline-band {
    position: absolute; left: 0; top: 400px; width: 100%; height: 130px;
    background: linear-gradient(180deg, rgba(11,11,11,0) 0%, rgba(11,11,11,0.75) 40%, var(--black) 100%);
    display: flex; align-items: flex-end; justify-content: center; padding-bottom: 18px;
  }
  .tagline {
    color: var(--white); font-size: 21px; line-height: 1.25; text-align: center;
  }
  .slogan-band {
    position: absolute; left: 0; top: 540px; width: 100%; height: 62px;
    background: linear-gradient(90deg, var(--gold-deep), var(--gold-light) 50%, var(--gold));
    display: flex; align-items: center; justify-content: center;
  }
  .slogan {
    color: var(--white); font-weight: 700; font-size: 22px; letter-spacing: 0.3px;
  }
  .front-web {
    position: absolute; left: 0; right: 0; top: 640px;
    text-align: center; color: var(--white); font-size: 14px; letter-spacing: 5px;
  }
</style>
</head>
<body>

  <section class="page back-cover">
    <h2 class="about-label">ABOUT</h2>
    <h3 class="about-heading">HARBORVALE VENTURES AND GENERAL PARTNER</h3>
    <div class="about-rule"></div>
    <p class="about-copy">Harborvale Ventures was founded in 2019 by General Partner Marcus Delane Jr with a group economic empowerment mission. Marcus Delane has invested in stocks since a teenager, received his BA in economics from Bayou Crest University and is currently attending Gulf Plains University.</p>

    <div class="back-panel">
      <div class="gold-band"></div>
      <div class="wordmark">Harborvale<br>Ventures</div>
    </div>

    <div class="about-photo" role="img" aria-label="Black and white photo of a city streetcar on a palm-lined avenue"></div>

    <ul class="contact-list">
      <li>
        <svg width="12" height="14" viewBox="0 0 12 14"><path d="M6 0a5 5 0 0 0-5 5c0 4 5 9 5 9s5-5 5-9a5 5 0 0 0-5-5zm0 7a2 2 0 1 1 0-4 2 2 0 0 1 0 4z" fill="#b39a3a"/></svg>
        <span>Address line 1, Address line 1<br>Address line 2.</span>
      </li>
      <li>
        <svg width="12" height="12" viewBox="0 0 12 12"><path d="M2.5 0.8l2 2-1 1.5c.7 1.6 1.9 2.8 3.5 3.5l1.5-1 2 2-1.3 1.8C5 10.5 1.5 7 .7 2.1z" fill="#b39a3a"/></svg>
        <span>0123 456 789</span>
      </li>
      <li>
        <svg width="12" height="12" viewBox="0 0 12 12"><circle cx="6" cy="6" r="5" fill="none" stroke="#b39a3a" stroke-width="1.2"/><path d="M1 6h10M6 1c2.5 3 2.5 7 0 10M6 1c-2.5 3-2.5 7 0 10" fill="none" stroke="#b39a3a" stroke-width="1"/></svg>
        <span class="web">www.HARBORVALEVENTURES.com</span>
      </li>
    </ul>
  </section>

  <section class="page front-cover">
    <header class="front-header">
      <div class="wordmark">Harborvale<span class="wordmark-sub">Ventures</span></div>
    </header>

    <div class="front-photo" role="img" aria-label="Businessman in a suit using a tablet, overlaid with a city skyline and rising stock chart lines"></div>

    <div class="tagline-band">
      <p class="tagline">Become a Partner and<br>Build Generational Wealth by Investing<br>In The Stock Market</p>
    </div>

    <div class="slogan-band">
      <p class="slogan">A First Of Its Kind Investment Club</p>
    </div>

    <p class="front-web">www.HarborvaleVentures.com</p>
  </section>

</body>
</html>
```